I need a design for my company's core values statement. This will be used on large posters (one as large as a wall), small posters, mouse pads, website, etc. I only need design, not content. The content should not change.

This is an IT company so it should be modern and impressive. Clean, sleek, professional are important guidelines. Our name is The Norvik Collective so space designs are not out of the question as long as they are not cliché or cheesey.

The values themselves should be the focus.

Here is the Core Values Statement as it is today:

THE NORVIK COLLECTIVE CORE VALUES

The Norvik Collective has resolved to make it clear to all stakeholders that we are a company which holds to certain core values and extolls the underlying virtues of that collective corporate conscience. Let it be known that following are the Core Values on which we base our personal behavior, our business dealings, and our daily decisions. Each member of the Norvik organization is held to these high standards on all levels of employment, interaction, and association.

THE NORVIK COLLECTIVE’S GUIDING PRINCIPLE:

“Treat everyone with the same high level of respect and care that customers receive.”
This principle applies to everyone we come in contact within the course of doing business while working for THE NORVIK COLLECTIVE. It pertains to clients of course, but also to colleagues, peers, subordinates, internal clients, vendors, and visitors.

OUR CORE VALUES

DELIVER EXCELLENCE
Exceed expectations.

BUILD TRUST
Through honesty, accountability, transparency, and accessibility.

BE A PEOPLE PERSON
Treat everyone with dignity and respect.

CREATE VALUE
Create and constantly deliver more value.
I
NNOVATE
Dream, innovate, create.

OWN IT
Take ownership.

Target Market(s)

International employees, clients, vendors

Industry/Entity Type

Business

Requirements
Must have
• Sleek, clean, modern, impressive. The values must be the focus
Nice to have
• We have a logo that I am attaching. it would be good to include, but not necessary.

```html
<!DOCTYPE html>
<html lang="en">
<head>
<meta charset="utf-8">
<title>The Norvik Collective — Our Core Values</title>
<link rel="stylesheet" href="https://fonts.googleapis.com/css2?family=Arimo:wght@700&family=Jura:wght@300;500&display=swap">
<style>
  :root {
    --blue: #1f8bcb;
    --green: #6bb240;
    --tagline: #8f8f8f;
    --body: #878787;
    --paper-light: #ffffff;
    --paper-edge: #d4d5d6;
  }
  html, body {
    margin: 0;
    width: 848px;
    height: 1200px;
    overflow: hidden;
  }
  .poster {
    width: 848px;
    height: 1200px;
    background: radial-gradient(ellipse 70% 60% at 50% 45%, var(--paper-light) 0%, #f1f1f1 45%, var(--paper-edge) 100%);
  }
  .poster svg { display: block; }
  .title-word { font-family: "Jura", sans-serif; font-weight: 500; fill: var(--green); }
  .value-name { font-family: "Jura", sans-serif; font-weight: 500; fill: var(--blue); }
  .value-line { font-family: "Jura", sans-serif; font-weight: 300; fill: var(--tagline); }
  .statement { font-family: "Arimo", sans-serif; font-weight: 700; fill: var(--body); font-size: 9.5px; }
</style>
</head>
<body>
<main class="poster">
  <svg width="848" height="1200" viewBox="0 0 848 1200" aria-label="The Norvik Collective core values">

    <g class="core-statement" transform="translate(285 145) rotate(-46)">
      <text class="statement">
        <tspan x="0" y="0">THE NORVIK COLLECTIVE</tspan>
        <tspan x="0" y="11">CORE VALUES</tspan>
        <tspan x="0" y="28">The Norvik Collective has</tspan>
        <tspan x="0" y="39">resolved to make it clear to</tspan>
        <tspan x="0" y="50">all stakeholders that we are a</tspan>
        <tspan x="0" y="61">company which holds to certain</tspan>
        <tspan x="0" y="72">core values and extolls the</tspan>
        <tspan x="0" y="83">underlying virtues of that collec-</tspan>
        <tspan x="0" y="94">tive corporate conscience. Let it</tspan>
        <tspan x="0" y="105">be known that following are the</tspan>
        <tspan x="0" y="116">Core Values on which we base</tspan>
        <tspan x="0" y="127">our personal behavior, our busi-</tspan>
        <tspan x="0" y="138">ness dealings, and our daily</tspan>
        <tspan x="0" y="149">decisions. Each member of the</tspan>
        <tspan x="0" y="160">Norvik organization is held to</tspan>
        <tspan x="0" y="171">these high standards on all</tspan>
        <tspan x="0" y="182">levels of employment,</tspan>
        <tspan x="0" y="193">interaction, and association.</tspan>
      </text>
    </g>

    <g class="poster-title">
      <text class="title-word" font-size="84" textLength="225" lengthAdjust="spacingAndGlyphs" transform="translate(222 192) rotate(46)">OUR</text>
      <text class="title-word" font-size="84" textLength="320" lengthAdjust="spacingAndGlyphs" transform="translate(177 236) rotate(46)">CORE</text>
      <text class="title-word" font-size="84" textLength="420" lengthAdjust="spacingAndGlyphs" transform="translate(132 280) rotate(46)">VALUES</text>
    </g>

    <g class="values-descending">
      <text class="value-name" font-size="70" textLength="420" lengthAdjust="spacingAndGlyphs" transform="translate(76 342) rotate(47)">INNOVATE</text>
      <text class="value-line" font-size="21" textLength="265" lengthAdjust="spacing" transform="translate(50 375) rotate(47)">Dream, innovate, create.</text>

      <text class="value-name" font-size="48" textLength="150" lengthAdjust="spacingAndGlyphs" transform="translate(180 580) rotate(47)">OWN IT</text>
      <text class="value-line" font-size="18" textLength="125" lengthAdjust="spacing" transform="translate(166 614) rotate(47)">Take ownership.</text>

      <text class="value-name" font-size="64" textLength="490" lengthAdjust="spacingAndGlyphs" transform="translate(377 748) rotate(40)">BUILD TRUST</text>
      <text class="value-line" font-size="14" textLength="415" lengthAdjust="spacing" transform="translate(362 790) rotate(39)">Through honesty, accountability, transparency, and accessibility.</text>

      <text class="value-name" font-size="48" textLength="370" lengthAdjust="spacingAndGlyphs" transform="translate(418 892) rotate(43)">CREATE VALUE</text>
      <text class="value-line" font-size="14" textLength="320" lengthAdjust="spacing" transform="translate(402 915) rotate(47)">Create and constantly deliver more value.</text>
    </g>

    <g class="values-ascending">
      <text class="value-name" font-size="72" textLength="815" lengthAdjust="spacingAndGlyphs" transform="translate(90 990) rotate(-46)">DELIVER EXCELLENCE</text>
      <text class="value-line" font-size="20" textLength="240" lengthAdjust="spacing" transform="translate(100 1028) rotate(-46)">Exceed expectations.</text>

      <text class="value-name" font-size="48" textLength="540" lengthAdjust="spacingAndGlyphs" transform="translate(432 722) rotate(-45.5)">BE A PEOPLE PERSON</text>
      <text class="value-line" font-size="18" textLength="380" lengthAdjust="spacing" transform="translate(455 735) rotate(-45)">Treat everyone with dignity and respect.</text>
    </g>

    <g class="guiding-principle" transform="translate(480 752) rotate(-45)">
      <text class="statement">
        <tspan x="0" y="0">THE NORVIK COLLECTIVE’S GUIDING PRINCIPLE:</tspan>
        <tspan x="0" y="14">“Treat everyone with the same high level of respect and care</tspan>
        <tspan x="0" y="25">that customers receive.”</tspan>
        <tspan x="0" y="36">This principle applies to everyone we come in contact within</tspan>
        <tspan x="0" y="47">the course of doing business while working for THE NORVIK</tspan>
        <tspan x="0" y="58">COLLECTIVE. It pertains to clients of course, but also to colleagues,</tspan>
        <tspan x="0" y="69">peers, subordinates, internal clients, vendors, and visitors.</tspan>
      </text>
    </g>
  </svg>
</main>
</body>
</html>
```